A poster for Vale Chiropractic's up coming powerful health workshop/seminar

I need a poster developed for Dr. Pruitt's upcoming Lasting Body Renewal and Armor Plating your Wellness seminar/workshop. This workshop will teach attendants how to shed pounds and rapidly reduce their waist size. Learn why weight loss doesn't work 99.9% of the time so that you can be the successful .1%. It's time to expose the LIES and reveal the TRUTH about the REAL causes of HEART DISEASE, DIABETES, CANCER, CHRONIC FATIGUE, ARTHRITIS, FIBROMYALGIA, and how to REVERSE/PREVENT this from ever happening to you or your family. The Insider Secrets to building your body into a health fortress unbreachable by sickness and disease. Learn to live and fufill your GOD-GIVEN health potential. Eliminate high bloodpressure, high cholesterol, diabetes, fatigue, chronic pain
Ending the WAR on sickness and disease by launching an unstoppable health offensive that will pummel any enemy of life and health.

I'm not a designer by any means, but was thinking of possible WAR theme, cammo, etc....just a thought. Not a requirement by any means
Updates

Dr. Pruitt has taken a look at all the submissions and has requested a few changes.

1. He wants the new map that has been added to the brief with Millbrook Valley College as a title above the map

2. He wants a section that describes what the attendees will gain at the seminar in bullet format.  Example:  Title....It's not about what you lose

                                                   I'ts about what you gain....

>The No-Hype, No- Gimmick  secrets for fast effective Weight loss

>How the top 3 disease killers, heart disease, cancer, and diabetes are linked to diet

>Tools and strategies to make 2012 the best year ever

The Seminar will be held at Millbrook Valley College, Tuesday January 3rd @ 6:30pm Open to Public

Target Market(s)

Adults 30-65

Industry/Entity Type

Building

Requirements
Should not have
• ruyrtur

```html
<!DOCTYPE html>
<html lang="en">
<head>
<meta charset="utf-8">
<title>Dr. Pruitt's Seminar — Lasting Body Renewal and Armor Plating Your Wellness</title>
<link href="https://fonts.googleapis.com/css2?family=Stardos+Stencil:wght@700&family=Cinzel:wght@600&family=Open+Sans:wght@600;700&display=swap" rel="stylesheet">
<style>
  :root {
    --bg-top: #0b3a47;
    --bg-mid: #17697c;
    --bg-bottom: #2a9db4;
    --ghost: rgba(8, 40, 50, 0.35);
    --ink: #ffffff;
    --panel: rgba(6, 36, 46, 0.55);
    --map-land: #cfd8c6;
    --map-road: #f4f1e6;
    --photo-dark: #1c2a33;
    --photo-light: #4f7d8c;
  }
  * { margin: 0; padding: 0; box-sizing: border-box; }
  html, body { width: 848px; height: 1200px; overflow: hidden; background: var(--bg-top); }
  .poster {
    position: relative;
    width: 848px;
    height: 1200px;
    overflow: hidden;
    background: linear-gradient(180deg, var(--bg-top) 0%, var(--bg-mid) 45%, var(--bg-bottom) 100%);
    color: var(--ink);
  }
  .ghost-words {
    position: absolute;
    inset: 0;
    font-family: "Stardos Stencil", serif;
    font-weight: 700;
    color: var(--ghost);
    font-size: 150px;
    line-height: 150px;
    white-space: nowrap;
    text-transform: uppercase;
    pointer-events: none;
  }
  .ghost-words span { display: block; }
  .ghost-words .r { text-align: right; }
  .ghost-words .small { font-size: 70px; line-height: 80px; }
  .presenter {
    position: absolute;
    top: 40px;
    left: 0;
    width: 100%;
    text-align: center;
    font-family: "Cinzel", serif;
    font-weight: 600;
  }
  .presenter .name { font-size: 50px; letter-spacing: 0.28em; line-height: 1; }
  .presenter .kind { font-size: 22px; letter-spacing: 0.5em; margin-top: 6px; }
  .title { position: absolute; top: 0; left: 0; width: 848px; height: 720px; }
  .title text {
    font-family: "Stardos Stencil", serif;
    font-weight: 700;
    fill: var(--ink);
    text-transform: uppercase;
  }
  .host-photo {
    position: absolute;
    left: 0;
    top: 745px;
    width: 305px;
    height: 455px;
    background: radial-gradient(ellipse at 50% 30%, var(--photo-light) 0%, var(--photo-dark) 70%);
    border-top-right-radius: 140px;
  }
  .highlights {
    position: absolute;
    left: 312px;
    top: 762px;
    width: 524px;
    list-style: none;
    font-family: "Open Sans", sans-serif;
    font-weight: 600;
    font-size: 13.5px;
    line-height: 17px;
  }
  .highlights li { position: relative; padding-left: 13px; margin-bottom: 7px; }
  .highlights li::before { content: "•"; position: absolute; left: 0; }
  .event {
    position: absolute;
    left: 312px;
    top: 1054px;
    width: 526px;
    height: 140px;
    display: flex;
    gap: 12px;
    padding: 8px 10px;
    background: var(--panel);
    font-family: "Open Sans", sans-serif;
    font-weight: 600;
  }
  .gains { flex: 1; }
  .gains h2 {
    font-family: "Stardos Stencil", serif;
    font-weight: 700;
    font-size: 15px;
    line-height: 17px;
    text-transform: uppercase;
  }
  .gains ul { list-style: none; margin-top: 5px; font-size: 11.5px; line-height: 14px; }
  .gains li { position: relative; padding-left: 11px; margin-bottom: 4px; }
  .gains li::before { content: "›"; position: absolute; left: 0; font-weight: 700; }
  .venue { width: 196px; display: flex; flex-direction: column; }
  .venue h3 {
    font-family: "Stardos Stencil", serif;
    font-weight: 700;
    font-size: 14px;
    line-height: 16px;
    text-transform: uppercase;
    text-align: center;
  }
  .venue-map {
    margin-top: 4px;
    height: 72px;
    background: linear-gradient(135deg, var(--map-land), var(--map-road));
  }
  .venue .when { margin-top: 5px; font-size: 11px; line-height: 14px; text-align: center; }
</style>
</head>
<body>
<main class="poster">
  <div class="ghost-words" aria-hidden="true">
    <span class="r small" style="margin-top:-10px">AND</span>
    <span class="r" style="margin-left:300px">ARMOR P</span>
    <span>LASTING</span>
    <span>BODY RENEW</span>
    <span>PLATING</span>
    <span>ARMOR</span>
    <span style="margin-left:60px">OUR WELLN</span>
    <span>LASTING</span>
  </div>

  <header class="presenter">
    <div class="name">Dr. Pruitt's</div>
    <div class="kind">Seminar</div>
  </header>

  <svg class="title" viewBox="0 0 848 720" role="heading" aria-level="1" aria-label="Lasting Body Renewal and Armor Plating Your Wellness">
    <text x="90" y="240" font-size="140" textLength="732" lengthAdjust="spacingAndGlyphs">Lasting</text>
    <text x="90" y="385" font-size="185" textLength="732" lengthAdjust="spacingAndGlyphs">Body</text>
    <text x="90" y="574" font-size="260" textLength="732" lengthAdjust="spacingAndGlyphs">Renewal</text>
    <text x="90" y="626" font-size="60" textLength="732" lengthAdjust="spacingAndGlyphs">And Armor Plating</text>
    <text x="90" y="703" font-size="88" textLength="732" lengthAdjust="spacingAndGlyphs">Your Wellness</text>
  </svg>

  <div class="host-photo" role="img" aria-label="Portrait photo of Dr. Pruitt in a dark suit and pink tie"></div>

  <ul class="highlights">
    <li>How to shed pounds and rapidly reduce their waist size</li>
    <li>Why weight loss doesn't work 99.9% of the time so that you can be the successful 0.1%</li>
    <li>Expose the LIES and reveal the TRUTH about the REAL causes of HEART DISEASE, DIABETES, CANCER, CHRONIC FATIGUE, ARTHRITIS, FIBROMYALGIA, and how to REVERSE/PREVENT this from ever happening to you or your family</li>
    <li>The Insider Secrets to building your body into a health fortress unbreachable by sickness and disease</li>
    <li>Learn to live and fulfill your GOD-GIVEN health potential</li>
    <li>Eliminate high bloodpressure, high cholesterol, diabetes, fatigue, chronic pain</li>
    <li>Ending the WAR on sickness and disease by launching an unstoppable health offensive that will pummel any enemy of life and health</li>
  </ul>

  <section class="event">
    <div class="gains">
      <h2>It's not about what you lose…<br>It's about what you gain…</h2>
      <ul>
        <li>The No-Hype, No-Gimmick secrets for fast effective weight loss</li>
        <li>How the top 3 disease killers, heart disease, cancer, and diabetes are linked to diet</li>
        <li>Tools and strategies to make 2012 the best year ever</li>
      </ul>
    </div>
    <div class="venue">
      <h3>Millbrook Valley College</h3>
      <div class="venue-map" role="img" aria-label="Street map showing the way to Millbrook Valley College"></div>
      <p class="when">Tuesday, January 3rd @ 6:30pm<br>Open to Public</p>
    </div>
  </section>
</main>
</body>
</html>
```